Full Page Ad for Coastal Dwelling Journal

we are The Garden Quarter an Outdoor design and construction company form Miami. see our website to get a better idea of who we are, what we do and our company profile. www.thegardenquarter-example.com

we need a full page ad for a luxury construction an architecture magazine. see magazine profile http://www.coastaldwelling-example.com/

design requirements:

use a minimum of 1 images or a maximum of 4 images from the files available

include Logo ( obviously )

include following text ( in no particular order):
"Outdoor Design & Construction / Outdoor Furniture "
"we create unique outdoor living spaces"
"thegardenquarter-example.com"
"Showroom: 4120 NW 62 Ave Miami, FL 33166"
"786.555.0142"

From the files uploaded see examples of ads that we like.

Specs:
Full Page
Final Trim : 8" x 10-7/8"
Live Area ( type) 7" x 10"
Bleed: 8.25" x 11.125"
Decimal equivalents: 8" x 10.875"

Reason: Really like the designs guys just want to see a few more options using some of the images that haven't been used yet. particularly the white structure attached to the house. thanks, TGQ Marketing team

```html
<!DOCTYPE html>
<html lang="en">
<head>
<meta charset="utf-8">
<title>The Garden Quarter — Full Page Ad</title>
<link rel="stylesheet" href="https://fonts.googleapis.com/css2?family=Mulish:wght@400;600;700&display=swap">
<style>
  :root {
    --page: #ffffff;
    --band-green: #7fb23f;
    --ink: #2b2b2b;
    --ink-soft: #3a3a3a;
    --brand-green: #5a9a2e;
    --frame: #ffffff;
  }
  * { margin: 0; padding: 0; box-sizing: border-box; }
  html, body { width: 890px; height: 1200px; overflow: hidden; background: var(--page); }
  body { font-family: "Mulish", "Helvetica Neue", Arial, sans-serif; color: var(--ink); }

  .ad { position: relative; width: 890px; height: 1200px; background: var(--page); }

  .hero-photo {
    position: absolute; left: 0; top: 0; width: 890px; height: 586px;
    background: linear-gradient(180deg,
      #7fa9cc 0%, #c9dbe8 12%, #f2f4f5 24%, #e4e9ea 32%,
      #7e9a76 38%, #3f6b3e 44%, #2e4f31 52%,
      #dfe4e4 58%, #f1f3f3 62%,
      #5fd0e6 66%, #39b9db 74%, #2a8fc2 84%,
      #2d4fa6 93%, #223a8a 100%);
  }

  .service-band {
    position: absolute; left: 0; top: 586px; width: 890px; height: 112px;
    background: var(--band-green);
  }
  .service-line {
    position: absolute; left: 0; top: 608px; width: 890px;
    text-align: center; color: #fff; font-size: 24px; font-weight: 400; line-height: 30px;
  }

  .gallery-photo {
    position: absolute; top: 652px; height: 172px;
    border: 5px solid var(--frame);
  }
  .gallery-photo.pool-house { left: 34px; width: 254px;
    background: linear-gradient(180deg, #a9c8e2 0%, #e3ecf2 28%, #eef0ef 45%, #6fa585 55%, #3d9fc4 70%, #2f7fae 82%, #e2e6e6 100%); }
  .gallery-photo.white-pavilion { left: 322px; width: 249px;
    background: linear-gradient(180deg, #8d5f3c 0%, #b88458 16%, #c7dbe8 24%, #f4f6f6 44%, #e6e8e8 62%, #cfd1cf 84%, #b3b1a8 100%); }
  .gallery-photo.cabana-lagoon { left: 606px; width: 251px;
    background: linear-gradient(180deg, #cdd7de 0%, #eceeed 34%, #5f7f4f 50%, #8aa078 58%, #d7ccb3 68%, #8fcfd6 80%, #d8ceb8 100%); }

  .tagline {
    position: absolute; left: 0; top: 856px; width: 890px;
    text-align: center; font-size: 24px; font-weight: 400; line-height: 30px; color: var(--ink);
  }

  .brand {
    position: absolute; left: 228px; top: 943px; height: 85px;
    display: flex; align-items: center; gap: 14px;
  }
  .brand-dot { width: 85px; height: 85px; flex: none; }
  .brand-name {
    font-size: 35px; font-weight: 600; color: var(--ink-soft); letter-spacing: 0.3px; white-space: nowrap;
  }

  .contact { position: absolute; left: 0; width: 890px; text-align: center; font-size: 19px; line-height: 24px; color: var(--ink); }
  .contact.web { top: 1078px; }
  .contact.showroom { top: 1113px; }
</style>
</head>
<body>
  <main class="ad">
    <div class="hero-photo" role="img" aria-label="Photo of a luxury backyard: raised blue-tiled spa in front of a large pool, dark pergolas with outdoor kitchen and lounge seating, palm trees under a cloudy blue sky"></div>

    <div class="service-band"></div>
    <p class="service-line">Outdoor Design &amp; Construction | Outdoor Furniture</p>

    <div class="gallery-photo pool-house" role="img" aria-label="Photo of a curved pool with spa beside a white modern house and palms"></div>
    <div class="gallery-photo white-pavilion" role="img" aria-label="Photo of a white modern structure attached to a house with wood ceiling and white lounge sofas"></div>
    <div class="gallery-photo cabana-lagoon" role="img" aria-label="Photo of a beach-entry lagoon pool with curtained cabana and palm trees"></div>

    <p class="tagline">we create unique outdoor living spaces.</p>

    <div class="brand">
      <svg class="brand-dot" viewBox="0 0 84 84" aria-hidden="true"><circle cx="42" cy="42" r="41" fill="var(--brand-green)"/></svg>
      <span class="brand-name">The Garden Quarter</span>
    </div>

    <p class="contact web">thegardenquarter-example.com</p>
    <p class="contact showroom">Showroom: 4120 NW 62 Ave | Miami, FL 33166 | 786.555.0142</p>
  </main>
</body>
</html>
```